Name card for fertilizer industry

We 1. produce liquid fertilizer 2. gardening supply 3. Import&Export gardening related product.
I want the name card double-sided(Chinese & English version)
detail has chinese charactor for name and address.
Updates
Target Market(s)
Farmers
Industry/Entity Type
Industry
Contact Information for Business Card
Name: Daniel Lo (陳明達)
TEL: +886-48-516042
FAX:+886-48-590714
MOBILE: +886-912-804-153
ADDRESS: No.58, Baoan Rd, Dapu Township, Kexi County , TAIWAN(R.O.C) 柯溪縣大埔鎮寶安路58號
Look and feel
Each slider illustrates characteristics of the customer's brand and the style your logo design should communicate.

```html
<!DOCTYPE html>
<html lang="zh-Hant">
<head>
<meta charset="utf-8">
<title>綠禾園 Business Card</title>
<link href="https://fonts.googleapis.com/css2?family=Questrial&family=Noto+Sans+TC:wght@400&display=swap" rel="stylesheet">
<style>
  :root {
    --bg: #e6e4e0;
    --brand-green: #5cb735;
    --card-white: #f3f3f3;
    --ink: #3a3a3a;
    --ink-soft: #6b6b6b;
    --mark-white: #ffffff;
  }
  * { box-sizing: border-box; margin: 0; padding: 0; }
  html, body {
    width: 1200px; height: 900px; overflow: hidden;
    background: var(--bg);
    font-family: "Questrial", "Noto Sans TC", sans-serif;
  }
  .stage {
    width: 1200px; height: 900px;
    display: flex; flex-direction: column;
    align-items: center; justify-content: center; gap: 56px;
  }
  .card {
    width: 640px; height: 366px; position: relative;
    box-shadow: 0 6px 18px rgba(0,0,0,.12);
  }
  .card--front { background: var(--brand-green); }
  .card--back { background: var(--card-white); }

  .brand {
    position: absolute; left: 50%; transform: translateX(-50%);
    display: flex; flex-direction: column; align-items: center; gap: 8px;
  }
  .card--front .brand { top: 112px; }
  .card--back .brand { top: 62px; }
  .brand__dot { width: 62px; height: 62px; border-radius: 50%; }
  .card--front .brand__dot { background: var(--mark-white); }
  .card--back .brand__dot { background: var(--brand-green); }
  .brand__name {
    font-family: "Noto Sans TC", sans-serif; font-weight: 400;
    font-size: 34px; letter-spacing: 4px; color: var(--ink);
  }

  .person { position: absolute; left: 48px; top: 96px; }
  .person__name {
    font-size: 13px; letter-spacing: 2.5px; text-transform: uppercase;
    color: var(--ink-soft);
  }
  .person__name-zh {
    font-family: "Noto Sans TC", sans-serif; font-size: 13px;
    letter-spacing: 2px; color: var(--ink-soft); margin-top: 4px;
  }
  .person__title { font-size: 12px; letter-spacing: 1.5px; color: var(--brand-green); margin-top: 4px; }

  .contact { position: absolute; left: 232px; top: 206px; color: var(--ink-soft); font-size: 12px; letter-spacing: 1px; }
  .contact__address { margin-left: 24px; line-height: 17px; margin-bottom: 6px; }
  .contact__address-zh { font-family: "Noto Sans TC", sans-serif; letter-spacing: 1.5px; }
  .contact__row { display: flex; align-items: center; gap: 10px; height: 18px; }
  .contact__icon { width: 13px; height: 13px; flex: none; }
  .contact__label { color: var(--brand-green); width: 52px; }
</style>
</head>
<body>
<main class="stage">
  <section class="card card--front" aria-label="Card front">
    <div class="brand">
      <span class="brand__dot"></span>
      <span class="brand__name">綠禾園</span>
    </div>
  </section>

  <section class="card card--back" aria-label="Card back">
    <div class="person">
      <p class="person__name">Daniel Lo</p>
      <p class="person__name-zh">陳明達</p>
      <p class="person__title">CEO</p>
    </div>

    <div class="brand">
      <span class="brand__dot"></span>
      <span class="brand__name">綠禾園</span>
    </div>

    <div class="contact">
      <p class="contact__address">No.58, Baoan Rd, Dapu Township, Kexi County,<br>TAIWAN(R.O.C)<br><span class="contact__address-zh">柯溪縣大埔鎮寶安路58號</span></p>
      <p class="contact__row">
        <svg class="contact__icon" viewBox="0 0 16 16"><path d="M3 1h3l1.5 4-2 1.3a9 9 0 0 0 4.2 4.2L11 8.5l4 1.5v3a2 2 0 0 1-2 2A12 12 0 0 1 1 3a2 2 0 0 1 2-2z" fill="var(--brand-green)"/></svg>
        <span class="contact__label">TEL</span><span>+886-48-516042</span>
      </p>
      <p class="contact__row">
        <svg class="contact__icon" viewBox="0 0 16 16"><rect x="4" y="1" width="8" height="4" fill="none" stroke="var(--brand-green)" stroke-width="1.5"/><rect x="1" y="5" width="14" height="7" rx="1" fill="var(--brand-green)"/><rect x="4" y="10" width="8" height="5" fill="var(--card-white)" stroke="var(--brand-green)" stroke-width="1.5"/></svg>
        <span class="contact__label">FAX</span><span>+886-48-590714</span>
      </p>
      <p class="contact__row">
        <svg class="contact__icon" viewBox="0 0 16 16"><rect x="4" y="1" width="8" height="14" rx="1.5" fill="none" stroke="var(--brand-green)" stroke-width="1.5"/><circle cx="8" cy="12.2" r="1" fill="var(--brand-green)"/></svg>
        <span class="contact__label">MOBILE</span><span>+886-912-804-153</span>
      </p>
      <p class="contact__row">
        <svg class="contact__icon" viewBox="0 0 16 16"><rect x="1" y="3" width="14" height="10" fill="none" stroke="var(--brand-green)" stroke-width="1.5"/><path d="M1 3l7 6 7-6" fill="none" stroke="var(--brand-green)" stroke-width="1.5"/></svg>
        <span class="contact__label">E-MAIL</span><span>daniel.lo@luhoyuan.tw</span>
      </p>
      <p class="contact__row">
        <svg class="contact__icon" viewBox="0 0 16 16"><circle cx="8" cy="8" r="6.5" fill="none" stroke="var(--brand-green)" stroke-width="1.5"/><path d="M1.5 8h13M8 1.5c-3 3.5-3 9.5 0 13M8 1.5c3 3.5 3 9.5 0 13" fill="none" stroke="var(--brand-green)" stroke-width="1.2"/></svg>
        <span class="contact__label">WEB</span><span>www.luhoyuan.tw</span>
      </p>
    </div>
  </section>
</main>
</body>
</html>
```